Create a bold and border around my logo to make it pop and sign graphic design

I would like someone to create a sign graphic design so I can use on the side of my trucks and put on yard signs. I would to remove a lot of the white and add more of the orange and blue to give it more pop when cars drive past. I would like the services to be removed and for you to leave space for a mobile number that i would add later. I don’t want my logo changed at all. I just want colour and design to be added to the background so i can use it in signage. Same colour as on the sign

```html
<!DOCTYPE html>
<html lang="en">
<head>
<meta charset="utf-8">
<title>Canopyworkers Sign</title>
<link rel="stylesheet" href="https://fonts.googleapis.com/css2?family=Montserrat:wght@800;900&display=swap">
<style>
  :root {
    --orange: #ee5a12;
    --border-blue: #1352c0;
    --panel-blue: #0c3f93;
    --white: #ffffff;
    --backdrop: #e9ebee;
  }
  html, body {
    margin: 0;
    padding: 0;
    width: 1200px;
    height: 905px;
    overflow: hidden;
    background: var(--backdrop);
  }
  .canvas {
    position: relative;
    width: 1200px;
    height: 905px;
  }
  .sign {
    position: absolute;
    left: 40px;
    top: 157px;
    width: 1120px;
    height: 590px;
    display: block;
  }
  .sign-text {
    font-family: "Montserrat", Arial, sans-serif;
    font-weight: 800;
  }
  .brand-name { fill: var(--white); font-size: 68px; }
  .phone-number { fill: var(--orange); font-size: 92px; font-weight: 900; }
</style>
</head>
<body>
<main class="canvas">
  <svg class="sign" viewBox="0 0 1120 590" xmlns="http://www.w3.org/2000/svg" aria-label="Canopyworkers yard sign with phone number">
    <!-- frame -->
    <rect class="frame" x="0" y="0" width="1120" height="590" fill="var(--orange)"/>
    <g class="frame-stripes" fill="var(--border-blue)">
      <polygon points="109,0 353,0 328,44 84,44"/>
      <polygon points="564,0 841,0 816,44 539,44"/>
      <polygon points="0,79 62,55 62,320 0,343"/>
      <polygon points="1058,70 1120,26 1120,290 1058,330"/>
      <polygon points="83,546 300,546 275,590 58,590"/>
      <polygon points="511,546 762,546 737,590 486,590"/>
    </g>
    <!-- inner panel -->
    <rect class="panel" x="62" y="44" width="996" height="502" fill="var(--orange)"/>
    <polygon class="panel-band" points="62,375 1058,240 1058,546 62,546" fill="var(--panel-blue)"/>
    <!-- brand mark placeholder -->
    <circle class="brand-dot" cx="538" cy="180" r="100" fill="var(--white)"/>
    <!-- name -->
    <text class="sign-text brand-name" x="163" y="349" textLength="740" lengthAdjust="spacingAndGlyphs">CANOPYWORKERS</text>
    <!-- phone box -->
    <rect class="phone-box" x="165" y="369" width="735" height="134" fill="var(--white)"/>
    <text class="sign-text phone-number" x="211" y="470" textLength="654" lengthAdjust="spacingAndGlyphs">0000 00 000</text>
  </svg>
</main>
</body>
</html>
```